Stationery Design Project for Lakemont Kenbu Kai Karate Studio

We Need a Stationery Design for a Karate School Teaching Okinawa Shorin Ryu Karate in Lakemont, Sunview, U.S.A.

Target Market(s)

Adults Base Western Speaking aged between 25 and 65 yrs, old that handle household budgets

Industry/Entity Type

School

Requirements
Must have
• Name of business: Lakemont Kenbu Kai Karate Studio
Address: Maplecrest Plaza 38214 US Hwy. 61
Lakemont, Sunview. 33812
Phone # : 407-555-0183
email : Lakemontkenbukaistudio@samplemail.net
Logo - attatched

```html
<!DOCTYPE html>
<html lang="en">
<head>
<meta charset="utf-8">
<title>Lakemont Kenbu Kai Karate Studio — Stationery</title>
<link rel="stylesheet" href="https://fonts.googleapis.com/css2?family=Oswald:wght@700&family=Questrial&display=swap">
<style>
  :root {
    --backdrop: #a8182e;
    --paper: #fbfbfb;
    --paper-shade: #eeeeee;
    --brand-red: #b3121f;
    --window: #6a1214;
    --ink: #111111;
    --contact-red: #b5162a;
    --strip: #2a0508;
    --strip-text: #f2d6d6;
  }
  * { margin: 0; padding: 0; box-sizing: border-box; }
  html, body { width: 1200px; height: 889px; overflow: hidden; }
  body { background: var(--backdrop); position: relative; font-family: "Questrial", sans-serif; }

  .sheet { position: absolute; overflow: hidden; }

  .letterhead { left: 193px; top: 66px; width: 364px; height: 515px; background: var(--paper); }
  .folder {
    left: 616px; top: 56px; width: 372px; height: 526px;
    background: radial-gradient(circle at 78% 52%, #c8192a 0%, #9e1420 45%, #5e0d10 100%);
  }
  .card {
    left: 61px; width: 167px; height: 97px;
    background: radial-gradient(circle at 50% 45%, #c01a26 0%, #8a1119 70%, #5a0b10 100%);
  }
  .card--one { top: 623px; }
  .card--two { top: 744px; }
  .card-strip {
    position: absolute; left: 0; right: 0; bottom: 0; height: 9px;
    background: var(--strip); color: var(--strip-text); font-size: 3px; line-height: 9px;
    display: flex; justify-content: space-between; padding: 0 5px; white-space: nowrap;
  }
  .envelope-front { left: 268px; top: 623px; width: 409px; height: 215px; background: var(--paper); }
  .envelope-back { left: 715px; top: 622px; width: 410px; height: 217px; background: var(--paper); }
  .envelope-window {
    position: absolute; left: 24px; top: 119px; width: 142px; height: 60px;
    border-radius: 10px; background: var(--window);
  }

  .wordmark {
    position: absolute; display: flex; flex-direction: column; align-items: center;
    font-family: "Oswald", sans-serif; font-weight: 700; color: var(--ink);
    text-transform: uppercase; line-height: 1; text-align: center;
  }
  .wordmark-dot { border-radius: 50%; background: var(--brand-red); margin-bottom: 4px; }
  .wordmark--small { font-size: 9px; }
  .wordmark--small .wordmark-dot { width: 16px; height: 16px; }
  .wordmark--card { font-size: 7px; }
  .wordmark--card .wordmark-dot { width: 12px; height: 12px; margin-bottom: 3px; }
  .wordmark--folder { font-size: 13px; }
  .wordmark--folder .wordmark-dot { width: 26px; height: 26px; background: var(--paper); }

  .contact { position: absolute; font-style: normal; font-size: 5.4px; line-height: 1.35; color: var(--contact-red); white-space: nowrap; }
  .contact-name { font-weight: 700; letter-spacing: 0.2px; }
  .contact-gap { height: 5px; }
</style>
</head>
<body>

  <section class="sheet letterhead" aria-label="Letterhead">
    <div class="wordmark wordmark--small" style="left:46px; top:52px;">
      <span class="wordmark-dot"></span>
      <span>Lakemont</span><span>Kenbu Kai</span><span>Karate</span>
    </div>
    <address class="contact" style="left:47px; top:444px;">
      <div class="contact-name">LAKEMONT</div>
      <div>Kenbu Kai Karate Studio</div>
      <div>Maplecrest Plaza 38214 US Hwy. 61</div>
      <div>Lakemont, Sunview. 33812</div>
      <div class="contact-gap"></div>
      <div>407-555-0183</div>
      <div>Lakemontkenbukaistudio@samplemail.net</div>
    </address>
  </section>

  <section class="sheet folder" aria-label="Presentation folder">
    <div class="wordmark wordmark--folder" style="left:246px; top:232px;">
      <span class="wordmark-dot"></span>
      <span>Lakemont</span><span>Kenbu Kai</span><span>Karate</span>
    </div>
  </section>

  <section class="sheet card card--one" aria-label="Business card">
    <div class="wordmark wordmark--card" style="left:58px; top:24px;">
      <span class="wordmark-dot"></span>
      <span>Lakemont</span><span>Kenbu Kai</span><span>Karate</span>
    </div>
    <div class="card-strip"><span>Maplecrest Plaza, Lakemont 33812</span><span>407-555-0183</span><span>Lakemontkenbukaistudio@samplemail.net</span></div>
  </section>

  <section class="sheet card card--two" aria-label="Business card">
    <div class="wordmark wordmark--card" style="left:58px; top:24px;">
      <span class="wordmark-dot"></span>
      <span>Lakemont</span><span>Kenbu Kai</span><span>Karate</span>
    </div>
    <div class="card-strip"><span>Maplecrest Plaza, Lakemont 33812</span><span>407-555-0183</span><span>Lakemontkenbukaistudio@samplemail.net</span></div>
  </section>

  <section class="sheet envelope-front" aria-label="Envelope front">
    <div class="wordmark wordmark--small" style="left:28px; top:28px; font-size:10px;">
      <span class="wordmark-dot"></span>
      <span>Lakemont</span><span>Kenbu Kai</span><span>Karate</span>
    </div>
    <address class="contact" style="left:292px; top:25px;">
      <div class="contact-name">LAKEMONT</div>
      <div>Kenbu Kai Karate Studio</div>
      <div>Maplecrest Plaza 38214 US Hwy. 61</div>
      <div>Lakemont, Sunview. 33812</div>
      <div class="contact-gap"></div>
      <div>407-555-0183</div>
      <div>Lakemontkenbukaistudio@samplemail.net</div>
    </address>
    <div class="envelope-window"></div>
  </section>

  <section class="sheet envelope-back" aria-label="Envelope back">
    <svg width="410" height="217" viewBox="0 0 410 217" aria-hidden="true">
      <path d="M0 0 H410 V40 Q410 58 392 60 L222 72 Q205 74 188 72 L18 60 Q0 58 0 40 Z" fill="var(--paper-shade)"/>
      <path d="M0 40 Q0 58 18 60 L188 72 Q205 74 222 72 L392 60 Q410 58 410 40" fill="none" stroke="#d8d8d8" stroke-width="1"/>
    </svg>
  </section>

</body>
</html>
```